Coastal Mulchworks Inc

Industry/Entity Type

Forestry

Contact Information for Business Card

Company name: Coastal Mulchworks INC, Contact Info: Rulemo Vantaro, Phone # 555 555 0187, Addres: 248 Whitlow Ferry Rd, Fernhollow ZZ 00000, Email: coastalmulchworks@examplemail.test

```html
<!DOCTYPE html>
<html lang="en">
<head>
<meta charset="utf-8">
<title>Coastal Mulchworks Inc — Business Cards</title>
<link rel="stylesheet" href="https://fonts.googleapis.com/css2?family=Montserrat:wght@300;400;600;700&display=swap">
<style>
  :root {
    --bark: #573314;
    --bark-band: #5d3817;
    --pine: #00873a;
    --tan: #94805d;
    --paper: #f4f4f2;
    --backdrop: #e6e6e4;
    --white: #ffffff;
  }
  * { margin: 0; padding: 0; box-sizing: border-box; }
  html, body { width: 1200px; height: 1199px; overflow: hidden; }
  body {
    position: relative;
    background: var(--backdrop);
    font-family: "Montserrat", Arial, sans-serif;
  }
  .card {
    position: absolute;
    top: 320px;
    width: 500px;
    height: 286px;
    border-radius: 4px;
    box-shadow: 0 10px 28px rgba(0,0,0,0.16);
  }
  .card--front {
    left: 60px;
    background: var(--paper);
    padding: 40px 40px 0 40px;
  }
  .card--back {
    left: 640px;
    background: var(--bark);
    display: flex;
    align-items: center;
    justify-content: center;
  }
  .wordmark {
    font-weight: 700;
    text-transform: uppercase;
    line-height: 1.05;
    letter-spacing: 0.5px;
  }
  .card--front .wordmark { color: var(--bark); font-size: 28px; }
  .card--back .wordmark { color: var(--white); font-size: 34px; text-align: left; }
  .divider {
    width: 44px;
    height: 2px;
    background: var(--bark);
    margin: 22px 0 20px;
  }
  .contact { list-style: none; color: var(--bark); font-size: 13.5px; line-height: 1.75; }
  .contact .label { font-weight: 300; }
  .contact .value { font-weight: 600; }
  .brand-band {
    position: absolute;
    left: 0; bottom: 0;
    width: 1200px;
    height: 255px;
    background: var(--bark-band);
    border-top: 16px solid var(--tan);
    display: flex;
    align-items: center;
    justify-content: center;
  }
  .brand-band .wordmark { color: var(--white); font-size: 48px; text-align: center; }
</style>
</head>
<body>
  <section class="card card--front" aria-label="Business card front">
    <div class="wordmark">Coastal<br>Mulchworks Inc</div>
    <div class="divider"></div>
    <ul class="contact">
      <li><span class="label">Contact Info: </span><span class="value">Rulemo Vantaro</span><span class="label"> | Phone: </span><span class="value">555 555 0187</span></li>
      <li><span class="label">Addres: </span><span class="value">248 Whitlow Ferry Rd, Fernhollow ZZ 00000</span></li>
      <li><span class="label">Email: </span><span class="value">coastalmulchworks@examplemail.test</span></li>
    </ul>
  </section>

  <section class="card card--back" aria-label="Business card back">
    <div class="wordmark">Coastal<br>Mulchworks Inc</div>
  </section>

  <footer class="brand-band">
    <div class="wordmark">Coastal<br>Mulchworks Inc</div>
  </footer>
</body>
</html>
```